Mediakit / brochure for Dutch Travel Blog

About our company:
• Bolderwijk.nl is a Travel- & influence network for independent travellers, outdoor geeks, culture lovers & adventure seekers.
• We don’t sell trips by ourself, we inspire other to travel.
• It’s all about travel inspiration.

About the media kit / brochure:
• The media kit itself must be a travel experience / inspiration.
• Colourful and clean design.
• Use the colours of our new logo
• Use our icons (marker, worldmap) in the design
• Use the style of our website.
• All the text in the media kit must be adjustable by us
• Page format: A4
• Number of pages: 6
• It must be printable as a brochure (for presentations)
• We also need a .pdf version of the brochure (for emailing it to our partners)
• Logo kit added: (1a) + (1b) + (1c) Logo sourcefile

Content of the media kit / brochure
• 6 pages
o (1) Front page
o (2) About Us
o (3) Stats / Companies work with
o (4) Advertising
o (5) Back page
o (6) Our contributors

• Example is attached: (2) example of a brochure with 5 pages A4 (don’t like the design of this example for our media kit, but just to show the idea of the 5 pages).

Maybe use a big travel photo that covers all pages?

For detailed information, I attached the document 'Design brochure Bolderwijk (version 2)'.
Updates

Hello designers,Small update for the Cover Page:- Please use one of the images from the attachment I added in the Brief Design: "URL of images for cover.txt"- Use this text "Travel- & influence network for independent travelers, outdoor geeks, culture lovers & adventure seekers."- Add the text MEDIA KIT (remove "2017: )Thanks.Hendrik Added Thursday, January 5, 2017

Target Market(s)

The mediakit / brochure is for our partners (travel organisations, airline companies, PR companies and big brands like Pale Timber Co and Vesko).

And the readers of our website are independent travellers, outdoor geeks and adventure seekers. So the theme of the Mediakit must be 'travel inspiration'.

Industry/Entity Type

Travel Industry

Requirements
Must have
• • The media kit itself must be a travel experience / inspiration.
• • Colourful and clean design.
• • Use the colours of our new logo
• • Use our icons (marker, worldmap) in the design
• • Use the style of our website.
• • All the text in the media kit must be adjustable by us
• • Page format: A4
• • Number of pages: 6
• • It must be printable as a brochure (for presentations)
• • We also need a .pdf version of the brochure (for emailing it to our partners)

```html
<!DOCTYPE html>
<html lang="en">
<head>
<meta charset="utf-8">
<title>Bolderwijk Media Kit</title>
<link href="https://fonts.googleapis.com/css2?family=Open+Sans:wght@400;600;700&display=swap" rel="stylesheet">
<style>
:root{
  --stage:#2b2b2b;
  --blue:#1b6fba;
  --ink:#2a2a2a;
  --muted:#555;
  --paper:#f1f1f1;
  --lime:#b5d334;
  --pink:#e8336e;
  --orange:#f7b12d;
  --cyan:#2fc0d6;
  --sky:#2d9de0;
  --red:#e2231a;
  --gold:#e8a317;
}
*{margin:0;padding:0;box-sizing:border-box}
html,body{width:1200px;height:680px;overflow:hidden}
body{background:var(--stage);font-family:"Open Sans",Arial,sans-serif;color:var(--ink);position:relative}
.brochure{position:absolute;left:30px;top:71px;width:1140px;height:538px;display:flex}
.panel{position:relative;width:380px;height:538px;overflow:hidden;background:var(--paper)}
.panel-bg{position:absolute;inset:0}
.abs{position:absolute}
h2{color:var(--blue);font-weight:700;font-size:16px;line-height:1}
.label{font-size:6.5px;color:var(--ink);text-transform:uppercase}
.small{font-size:5.6px;line-height:1.45;color:var(--ink)}

/* audience */
.gender-figure{position:absolute;width:11px;height:29px;border-radius:5px 5px 3px 3px}
.gender-pct{position:absolute;font-size:7.5px;font-weight:700}
.age-row{position:absolute;left:161px;height:9px;display:flex;align-items:center}
.age-bar{height:9px;font-size:6px;color:#fff;padding-left:5px;line-height:9px}
.age-val{font-size:9.5px;font-weight:700;margin-left:6px;color:var(--ink)}
.map-area{position:absolute;left:38px;top:197px;width:106px;height:48px;border-radius:14px 20px 10px 18px;background:linear-gradient(100deg,#2479c4,#1b6fba)}
.map-badge{position:absolute;left:95px;top:195px;background:var(--red);color:#fff;font-size:7px;font-weight:700;padding:1px 3px}
.social-row{position:absolute;left:38px;top:290px;display:flex;gap:6px;font-size:6.5px;font-weight:600;white-space:nowrap}
.social{display:flex;align-items:center}
.social-sq{width:9px;height:9px;background:var(--blue);margin-right:3px}
.social-name{margin-right:3px;color:var(--blue)}
.stat-num{position:absolute;left:216px;font-size:10px;font-weight:700;color:var(--ink)}
.stat-lbl{position:absolute;right:30px;font-size:9px;font-weight:700;color:var(--gold);text-align:right;line-height:1}
.stat-lbl small{display:block;font-size:3.5px;color:var(--muted);font-weight:400}
.partner{position:absolute;font-size:10px;font-weight:700;color:var(--blue);transform:translateX(-50%);white-space:nowrap}
.footer{position:absolute;top:518px;font-size:8.5px;color:var(--blue);display:flex;align-items:center}
.footer i{display:inline-block;width:8px;height:6px;border:1px solid var(--gold);margin-right:5px}
.footer i.round{height:8px;border-radius:50%}

/* about */
.about{position:absolute;left:28px;top:37px;width:188px}
.about p{font-size:7.6px;line-height:1.38;color:var(--blue);text-align:justify;margin-top:9px}
.about p b{color:var(--ink);font-weight:600}

/* services */
.service-list{position:absolute;left:39px;top:175px;width:325px;display:flex;flex-direction:column;gap:3px}
.service h3{font-size:8.8px;font-weight:600;color:var(--blue);display:flex;align-items:center;margin-left:-14px;line-height:12px}
.service h3::before{content:"";width:8px;height:8px;border-radius:50%;background:var(--sky);margin-right:6px}
.pricing{position:absolute;right:35px;top:461px;font-size:7.5px;font-weight:700}
</style>
</head>
<body>
<div class="brochure">

  <!-- Panel: stats & partners -->
  <section class="panel panel-stats">
    <svg class="panel-bg" width="380" height="538" viewBox="0 0 380 538">
      <defs>
        <linearGradient id="photoA" x1="0" y1="0" x2="1" y2="1">
          <stop offset="0" stop-color="#0d1620"/><stop offset=".6" stop-color="#4a6c8c"/><stop offset="1" stop-color="#c9d7e4"/>
        </linearGradient>
        <linearGradient id="footA" x1="0" y1="0" x2="0" y2="1">
          <stop offset="0" stop-color="#fafafa"/><stop offset="1" stop-color="#c4c4c4"/>
        </linearGradient>
      </defs>
      <rect width="380" height="130" fill="url(#photoA)" role="img" aria-label="Photo of a snowy forest with dark branches"/>
      <path d="M0,100 Q170,20 380,52 L380,300 L0,300Z" fill="var(--blue)"/>
      <path d="M0,110 Q170,34 380,63 L380,300 L0,300Z" fill="#fff"/>
      <path d="M0,116 Q170,42 380,70 L380,538 L0,538Z" fill="var(--paper)"/>
      <path d="M0,438 Q170,520 380,462 L380,538 L0,538Z" fill="var(--blue)"/>
      <path d="M0,452 Q170,528 380,474 L380,538 L0,538Z" fill="#fff"/>
      <path d="M0,458 Q170,534 380,480 L380,538 L0,538Z" fill="url(#footA)"/>
    </svg>

    <h2 class="abs" style="left:38px;top:114px">Audience Overview</h2>

    <div class="label abs" style="left:38px;top:142px">Gender</div>
    <div class="gender-figure" style="left:76px;top:147px;background:var(--pink)"></div>
    <div class="gender-pct" style="left:92px;top:147px;color:var(--pink)">46%</div>
    <div class="gender-pct" style="left:92px;top:160px;color:var(--sky)">54%</div>
    <div class="gender-figure" style="left:117px;top:145px;background:var(--sky)"></div>

    <div class="label abs" style="left:199px;top:142px">Age</div>
    <div class="age-row" style="top:157px"><div class="age-bar" style="width:91px;background:var(--lime)">18-24</div><span class="age-val">27%</span></div>
    <div class="age-row" style="top:172px"><div class="age-bar" style="width:114px;background:var(--pink)">25-34</div><span class="age-val">30%</span></div>
    <div class="age-row" style="top:186px"><div class="age-bar" style="width:67px;background:var(--orange)">35-44</div><span class="age-val">20%</span></div>
    <div class="age-row" style="top:201px"><div class="age-bar" style="width:47px;background:var(--cyan)">45-54</div><span class="age-val">13%</span></div>
    <div class="age-row" style="top:215px"><div class="age-bar" style="width:21px;background:var(--pink)">55-64</div><span class="age-val">5%</span></div>
    <div class="age-row" style="top:230px"><div class="age-bar" style="width:21px;background:var(--sky)">65+</div><span class="age-val">5%</span></div>

    <div class="label abs" style="left:38px;top:178px">Countries visited</div>
    <div class="map-area" role="img" aria-label="World map highlighting countries visited"></div>
    <div class="map-badge">81%</div>

    <h2 class="abs" style="left:38px;top:259px">Traffic &amp; Social Media</h2>
    <div class="social-row">
      <div class="social"><span class="social-sq"></span><span class="social-name">Pagely</span>35.000</div>
      <div class="social"><span class="social-sq"></span><span class="social-name">Chirply</span>7000</div>
      <div class="social"><span class="social-sq"></span><span class="social-name">Lensly</span>6000</div>
    </div>
    <div class="stat-num" style="top:281px">240.000</div>
    <div class="stat-num" style="top:298px">115.000</div>
    <div class="stat-lbl" style="top:282px">PAGE VIEWS<small>*MONTHLY</small></div>
    <div class="stat-lbl" style="top:299px">UNIQUE VISITORS<small>*MONTHLY</small></div>

    <h2 class="abs" style="left:38px;top:320px">Companies We Work With</h2>
    <p class="small abs" style="left:38px;top:342px;width:305px">Wondering how to transform your product from a commodity into an experience? Not sure how to leverage the power of social media and connect with your target demographic? Need help aligning your branding with your company values? Whether you are a tourism board, travel company, property, or product, we can help. We work with more than 100 travel- and brand partners.</p>

    <div class="partner" style="left:57px;top:392px">Aerlyn</div>
    <div class="partner" style="left:118px;top:392px">Tovi</div>
    <div class="partner" style="left:178px;top:392px">Corala</div>
    <div class="partner" style="left:262px;top:392px">Skyvane</div>
    <div class="partner" style="left:330px;top:392px">Rolvka</div>
    <div class="partner" style="left:57px;top:432px">Vesko</div>
    <div class="partner" style="left:155px;top:432px">Routemark</div>
    <div class="partner" style="left:257px;top:432px">Fjordal</div>
    <div class="partner" style="left:327px;top:432px;font-size:8px">Pale Timber Co</div>

    <div class="footer" style="left:45px"><i></i>info@bolderwijk.nl</div>
    <div class="footer" style="left:246px"><i class="round"></i>www.bolderwijk.nl</div>
  </section>

  <!-- Panel: about -->
  <section class="panel panel-about">
    <div class="panel-bg" role="img" aria-label="Photo of a traveller in a knitted hat sitting by a campfire in the snow" style="background:linear-gradient(180deg,#e9eef3 0%,#dfe6ee 35%,#8a95a2 60%,#3b3c3e 80%,#2a2520 100%)"></div>
    <div class="about">
      <h2>About Us</h2>
      <p>Bolderwijk is leading in travel inspiration in The Netherlands. <b>Our impassioned team</b> of travel journalists, bloggers , and vloggers create travel stories about independent &amp; off the beaten track travel, near and afar. Created in 2007, Bolderwijk began as a personal backpack blog that has now turned into an <b>award winning travel platform.</b></p>
      <p>Our blog is all about providing inspiration for your own journeys no matter how big or small. We love documenting the world around us, seeking out eclectic travel moments and <b>inspiring others to live the life they desire.</b> Our knowledge of the world's most inspiring places is unrivalled.</p>
      <p>The travel stories by Bolderwijk show us that we can conquer the world, get lost in its beauty, and find ourselves wherever our feet (or passport) may take us. We take our readers and fans on a <b>digital journey around the world</b> in search of the beautiful, the unusual, the forgotten and the mundane. Sit down, relax and have a browse of our inspiring travel stories and videos on <b>www.bolderwijk.nl.</b></p>
    </div>
  </section>

  <!-- Panel: services -->
  <section class="panel panel-services">
    <svg class="panel-bg" width="380" height="538" viewBox="0 0 380 538">
      <defs>
        <linearGradient id="photoC" x1="0" y1="0" x2="0" y2="1">
          <stop offset="0" stop-color="#6f6a62"/><stop offset="1" stop-color="#d8d4cc"/>
        </linearGradient>
        <linearGradient id="footC" x1="0" y1="0" x2="0" y2="1">
          <stop offset="0" stop-color="#fafafa"/><stop offset="1" stop-color="#c4c4c4"/>
        </linearGradient>
      </defs>
      <rect width="380" height="120" fill="url(#photoC)" role="img" aria-label="Photo of penguins on a rocky beach"/>
      <path d="M0,88 Q170,30 380,45 L380,300 L0,300Z" fill="var(--blue)"/>
      <path d="M0,98 Q170,44 380,56 L380,300 L0,300Z" fill="#fff"/>
      <path d="M0,104 Q170,52 380,63 L380,538 L0,538Z" fill="var(--paper)"/>
      <path d="M0,445 Q180,530 380,455 L380,538 L0,538Z" fill="var(--blue)"/>
      <path d="M0,459 Q180,537 380,468 L380,538 L0,538Z" fill="#fff"/>
      <path d="M0,465 Q180,543 380,474 L380,538 L0,538Z" fill="url(#footC)"/>
    </svg>

    <div class="abs" style="left:39px;top:113px;width:15px;height:15px;border-radius:50%;background:var(--blue)"></div>
    <h2 class="abs" style="left:79px;top:113px">Let's Work Together</h2>
    <p class="small abs" style="left:39px;top:134px;width:310px">Bolderwijk has a large online interactive community through its readers and social networks that provides a perfect venue to showcase your brand or destination to a highly engaged online audience of travel enthusiasts.</p>
    <div class="abs" style="left:39px;top:157px;font-size:9px;font-weight:600">Check out some of the things we can do for you.</div>

    <div class="service-list">
      <div class="service"><h3>Travel Writing</h3><p class="small">Yes please! Digital Storytelling our core business. About independent &amp; off the beaten path travel. About exciting cities, with their buzzing street life, wild nightlife and unbeatable attractions. About otherworldly landscapes and awe-inspiring natural wonders. Near and afar.</p></div>
      <div class="service"><h3>Press &amp; Fam Trips</h3><p class="small">The only thing we love more than experiencing new places is sharing the destinations with our readers. Our travel journalists are invited by tourist offices, airline companies, hotel brands and other partners. In 2016 for example our journalists went to Peru, Norway, South Africa, Costa Rica, Thailand and Spitsbergen.</p></div>
      <div class="service"><h3>Reviews / Sponsorship</h3><p class="small">We love reviews! They give us a chance to let our readers know about unique products for the experiential traveler. We'd love to write an honest review for your app, product, hotel or anything else you can think of!</p></div>
      <div class="service"><h3>Travel directory</h3><p class="small">Are you the owner of a small romantic B&amp;B in Italy? Or of that cool rafting company in Bali? Or do you have an excellent restaurant on Aruba? We invented our unique traveldirectory for local companies, where we match accommodations, attractions, tours, travelcompanies and restaurants to a specific destination.</p></div>
      <div class="service"><h3>Advertising</h3><p class="small">Advertorials, SEO articles, sidebars, banners, social media promotion. We have a lot of interesting advertising opportunities to help your business market its products and services to a target audience and help you expand your brand awareness.</p></div>
      <div class="service"><h3>Photography</h3><p class="small">It's no secret that stunning images are one of the best and easiest ways to showcase your brand or destination. We offer a selection of photography services that help enhance your brands website and social networks.</p></div>
      <div class="service"><h3>Travelvlogs</h3><p class="small">Professionally produced and edited videos. Showcase your destination through the eyes of a world traveler!</p></div>
      <div class="service"><h3>Videography using drones</h3><p class="small">Our state of the art drone footages will blow your mind.</p></div>
    </div>

    <div class="pricing">Please ask for current pricing</div>
    <div class="abs" role="img" aria-label="Colourful globe emblem" style="left:150px;top:466px;width:52px;height:52px;border-radius:50%;background:linear-gradient(135deg,#e8336e,#2fc0d6 55%,#f7b12d)"></div>
  </section>

</div>
</body>
</html>
```